Web Design Project for Brightpath Cable Collective

Design a webpage to replace www.brightpathcablecollective.com.au

View the website and design a new website based on the same philosophy of the original.

The website will be fresh, simple, elegant, modern, and a hint of high degree of technical backdrop.

Please utilise the logo in the website design and keep the different contents.

Industry/Entity Type

Group

Requirements
Must have
• Must incorporate the logo which will be uploaded.

```html
<!DOCTYPE html>
<html lang="en">
<head>
<meta charset="utf-8">
<title>Brightpath Cable Collective</title>
<link rel="stylesheet" href="https://fonts.googleapis.com/css2?family=Arimo:wght@400;700&display=swap">
<style>
:root{
  --page:#e9ebed;
  --page-low:#f7f8f8;
  --rule:#9aa0a5;
  --ink:#333638;
  --body:#5b5f62;
  --brand:#1f6b3a;
  --green:#8cc22a;
  --btn-green:#557f1f;
  --btn-green-dark:#3f6215;
  --amber:#f6c21a;
  --side:#c9c9c9;
  --side-fold:#8f9397;
  --footer:#a6aeb5;
  --white:#ffffff;
  --orange:#f08a1e;
  --blue:#2a6fb5;
  --sky:#3aa5dd;
}
*{box-sizing:border-box;margin:0;padding:0}
html,body{width:1047px;height:1200px;overflow:hidden}
body{position:relative;font-family:"Arimo",Arial,sans-serif;color:var(--body);
  background:linear-gradient(180deg,#dfe2e5 0,#e6e8ea 200px,var(--page) 560px,var(--page-low) 1100px)}
.abs{position:absolute}
.top-rule{left:21px;top:10px;width:1005px;height:6px;background:var(--rule);border-radius:2px}
.header-shade{left:21px;top:16px;width:1005px;height:172px;background:linear-gradient(180deg,#e6e8ea,#d6d9dc)}
.brand{left:39px;top:58px;display:flex;align-items:center;gap:12px}
.brand-mark{width:44px;height:44px;border-radius:50%;background:var(--brand)}
.brand-name{font-size:25px;font-weight:700;color:var(--brand);letter-spacing:-.2px}
.search{left:798px;top:80px;width:207px;height:27px;background:#9ea5ab;border:1px solid #c4c8cb;
  color:var(--white);font-size:14px;padding:5px 15px}
.search svg{position:absolute;right:6px;top:4px}
.nav{left:21px;top:140px;width:1005px;height:48px}
.nav a{position:absolute;bottom:0;width:123px;height:36px;border-radius:8px 8px 0 0;
  background:linear-gradient(180deg,#fdfdfd,#d9dbdd);border:1px solid #c9ccce;border-bottom:none;
  text-align:center;font-size:13px;color:#222;text-decoration:none;padding-top:13px}
.nav a.current{height:48px;padding-top:17px;background:linear-gradient(180deg,#ffffff,#dcdedf)}
.hero{left:21px;top:188px;width:1005px;height:361px;border-radius:0 0 6px 6px;overflow:hidden;
  background:radial-gradient(circle at 28% 30%,#a4d83a 0,var(--green) 40%,#86bd24 100%);
  box-shadow:0 2px 3px rgba(0,0,0,.25)}
.hero-photo{position:absolute;left:42px;top:0;width:482px;height:361px;
  background:radial-gradient(ellipse at 40% 55%,#3a4656 0,#2d3540 35%,rgba(60,70,80,0) 70%)}
.hero-title{position:absolute;left:553px;top:122px;color:var(--white);font-weight:700;
  font-size:34px;line-height:44px;text-shadow:1px 2px 2px rgba(0,0,0,.35)}
.hero-title .big{font-size:40px}
.btn{position:absolute;display:flex;align-items:center;justify-content:center;border-radius:3px;
  box-shadow:1px 2px 2px rgba(0,0,0,.3)}
.btn-learn{left:607px;top:253px;width:118px;height:42px;background:var(--btn-green);color:var(--white);font-size:16px}
.btn-projects{left:777px;top:253px;width:118px;height:42px;background:var(--amber);color:#222;font-size:16px}
.welcome{left:21px;top:574px;font-size:25px;font-weight:700;color:var(--ink);text-shadow:1px 1px 1px rgba(0,0,0,.2)}
.intro{left:21px;top:634px;width:700px;font-size:12.6px;line-height:19px}
.intro p{margin-bottom:19px}
.points{left:46px;top:849px;list-style:none;font-size:12.6px;color:#222}
.points li{height:27px;position:relative;padding-left:13px}
.points li::before{content:"";position:absolute;left:0;top:6px;width:6px;height:6px;border-radius:50%;background:#aab0b4}
.btn-read{left:625px;top:888px;width:83px;height:28px;font-size:12.6px;color:var(--white);
  background:linear-gradient(180deg,#5e8a25,var(--btn-green-dark));border:1px solid #375411}
.divider{left:61px;top:941px;width:621px;height:1px;background:#a9adb0}
.sub-head{font-size:18px;font-weight:700;color:var(--ink)}
.newsletter-head{left:21px;top:964px}
.email{left:28px;top:1014px;width:240px;height:30px;background:#cfd3d6;border:1px solid #a5abaf;
  border-radius:2px;font-size:12.6px;color:#4d5255;padding:7px 13px}
.btn-sub{left:185px;top:1056px;width:83px;height:30px;font-size:12.6px;color:var(--white);
  background:linear-gradient(180deg,#5e8a25,var(--btn-green-dark));border:1px solid #375411}
.featured-head{left:335px;top:964px}
.featured-arrows{left:681px;top:962px;font-size:14px;color:#9a9ea2;letter-spacing:2px}
.featured{left:334px;top:1001px;list-style:none;font-size:12.6px;color:#4d5255}
.featured li{height:25px;padding-left:27px;position:relative}
.featured li svg{position:absolute;left:0;top:1px}
.sidebar{left:729px;top:552px;width:287px;height:550px;background:var(--side)}
.side-head{position:absolute;left:729px;width:297px;height:34px;background:linear-gradient(180deg,#f1f2f2,#dcdedf);
  font-size:18px;font-weight:700;color:var(--ink);padding:6px 15px}
.side-head::after{content:"";position:absolute;right:0;bottom:-10px;border-top:10px solid var(--side-fold);border-right:10px solid transparent}
.rss-box{display:inline-block;width:16px;height:16px;background:var(--orange);border-radius:3px;margin-left:4px;vertical-align:-1px}
.news{left:753px;font-size:12.6px;line-height:19px;color:#222;width:250px}
.news .date{font-weight:700;color:#555}
.news .link{color:var(--white);text-decoration:underline}
.testimonial-photo{left:745px;top:872px;width:72px;height:59px;background:linear-gradient(180deg,#d8ccc0,#8a6d5c)}
.testimonial{left:828px;top:874px;width:180px;font-size:12.6px;line-height:19px;color:#555}
.testimonial b{color:#222}
.contact{left:761px;top:998px;font-size:12.6px;line-height:19px;color:#555}
.footer{left:0;top:1102px;width:1047px;height:98px;background:var(--footer)}
.foot-links{left:0;width:1047px;top:1132px;text-align:center;font-size:14px;color:var(--white)}
.foot-links span{margin:0 4px}
.copy{left:0;width:1047px;top:1164px;text-align:center;font-size:14px;color:var(--white)}
.connect{left:916px;top:1132px;font-size:14px;color:var(--white)}
.social{top:1152px;width:29px;height:29px;border-radius:4px}
</style>
</head>
<body>
<div class="abs header-shade"></div>
<div class="abs top-rule"></div>

<div class="abs brand"><span class="brand-mark"></span><span class="brand-name">Brightpath Cable Collective</span></div>

<div class="abs search">Search
  <svg width="18" height="18" viewBox="0 0 18 18"><circle cx="7" cy="7" r="5.5" fill="none" stroke="#fff" stroke-width="1.6"/><line x1="11" y1="11" x2="16.5" y2="16.5" stroke="#fff" stroke-width="2"/></svg>
</div>

<nav class="abs nav">
  <a class="current" style="left:0">Home</a>
  <a style="left:126px">Mission</a>
  <a style="left:252px">Services</a>
  <a style="left:377px">Products</a>
  <a style="left:503px">Partners</a>
  <a style="left:628px">Contact</a>
  <a style="left:754px">Online shop</a>
  <a style="left:880px">Blog</a>
</nav>

<section class="abs hero">
  <div class="hero-photo" role="img" aria-label="Smiling businessman in a dark suit pointing at an open laptop"></div>
  <h2 class="hero-title">ACHIVE THE <span class="big">HIGHEST</span><br>RESULTS</h2>
  <a class="btn btn-learn">Learn more</a>
  <a class="btn btn-projects">Projects info</a>
</section>

<h1 class="abs welcome">Welcome to Brightpath Cable Collective</h1>
<div class="abs intro">
  <p>Brightpath Cable Collective provides products and services through an integrated approach for reliable, mature and flexible solutions. Solutions that provide scale from single business premise to multinational offices through-out the world. We understand solutions need to be tailored to your needs; we keep in mind your growth in the years to come.</p>
  <p>Allow us the opportunity to unify your network...</p>
  <p>We are an Electrical Engineering consulting company specialising in consultation, supply, installation and service of electrical and communications systems. From design to implementation and continuing service management, we assist in managing your solution as you grow. By offering a unified network of goods and service providers, the quality of your electrical and communication solutions become integrated from the very first design through to future service management requirements.</p>
</div>
<ul class="abs points">
  <li>Unified in collaborations.</li>
  <li>Unified in solutions.</li>
  <li>Brightpath Cable Collective by nature.</li>
</ul>
<a class="abs btn btn-read">Read more</a>
<div class="abs divider"></div>

<h3 class="abs sub-head newsletter-head">News letter</h3>
<div class="abs email">Your e-mail id here</div>
<a class="abs btn btn-sub">Subscribe</a>

<h3 class="abs sub-head featured-head">Featured Services</h3>
<div class="abs featured-arrows">‹›</div>
<ul class="abs featured">
  <li><svg width="15" height="15" viewBox="0 0 15 15"><circle cx="7.5" cy="7.5" r="7" fill="#d3d6d8"/><path d="M6 4.5 9.5 7.5 6 10.5z" fill="#fff"/></svg>Lorem ipsum dolor sit amet con sectetuer mauris vel tortor</li>
  <li><svg width="15" height="15" viewBox="0 0 15 15"><circle cx="7.5" cy="7.5" r="7" fill="#d3d6d8"/><path d="M6 4.5 9.5 7.5 6 10.5z" fill="#fff"/></svg>Lorem ipsum dolor sit amet con sectetuer mauris vel tortor</li>
  <li><svg width="15" height="15" viewBox="0 0 15 15"><circle cx="7.5" cy="7.5" r="7" fill="#d3d6d8"/><path d="M6 4.5 9.5 7.5 6 10.5z" fill="#fff"/></svg>Lorem ipsum dolor sit amet con sectetuer mauris vel tortor</li>
</ul>

<aside class="abs sidebar"></aside>
<div class="side-head" style="top:578px">Latest News<span class="rss-box"></span></div>
<div class="abs news" style="top:630px">
  <div class="date">20 Dec. 2010</div>
  <div class="link">Race your car to the finish line</div>
  <div>Lorem ipsum dolor sit amet consectetuer mauris vel tortor vitae nibh condimentum.</div>
</div>
<div class="abs news" style="top:717px">
  <div class="date">20 Dec. 2010</div>
  <div class="link">Race your car to the finish line</div>
  <div>Lorem ipsum dolor sit amet consectetuer mauris vel tortor vitae nibh condimentum.</div>
</div>

<div class="side-head" style="top:816px">Testimonials</div>
<div class="abs testimonial-photo" role="img" aria-label="Portrait of a client giving a testimonial"></div>
<div class="abs testimonial"><b>Contrary to popular belief,</b><br>Lorem Ipsum is not simply roots in a piece of classical</div>

<div class="side-head" style="top:956px">Contact Us</div>
<div class="abs contact">
  BCC PTY. LTD.<br>ACN: 482 903 517<br>ABN: 31 482 903 517<br>FAX: +61 2 9000 4812<br>Mail: PO.Box 318 Ultimo, NSW,
</div>

<footer class="abs footer"></footer>
<div class="abs foot-links">home <span>|</span> mission <span>|</span> services <span>|</span> products <span>|</span> partners <span>|</span> contact <span>|</span> online shop <span>|</span> blog</div>
<div class="abs copy">All © Copyrights.brightpathcablecollective.reserved</div>
<div class="abs connect">Connect with us:</div>
<div class="abs social" style="left:924px;background:var(--blue)"></div>
<div class="abs social" style="left:958px;background:var(--sky)"></div>
<div class="abs social" style="left:993px;background:var(--orange)"></div>
</body>
</html>
```